STICKER DESIGN required for packaging. UK START UP TEA BUSINESS

We are looking for a design for a sticker that will be applied to packaging for our teas! We are a new start up Tea business based in the UK called 'BrookLeafs'
Selling quality loose leaf tea and teabags via our online shop and also face to face at farmers markets / food shows and eventually in our own tea emporium. We will be marketing our teas to hotels, cafes, delis etc. too
We carry every day teas eg. breakfast blends and also speciality and rare teas to offer customers the chance to try something new. Tea as a treat / ritual / indulgence / healthy lifestyle choice / modern
The design will initially be printed on vinyl stickers and then applied to the tea packaging (pouch bags in matte black and matte silver), in the future the design may be printed direct onto our packaging. The sticker design will need to be scalable as the size of the pouch bag varies dependant on the tea.
The sticker we have in mind is a leaf shape (sketch attached)
colour green to match our logo
It will include our logo (files attached)
Text to be included on the sticker is
- www.brookleafs.co.uk
- Welbury, England
- The tea type eg. Green
It will need to complement both black and silver pouches that we are using to package our teas (see attached image of our pouches)
Colours - green leaf, see our corporate colours (green & orange) on our logo files attached. We also like silver and black.
Font - nothing to swirly, must be easy to read on the packaging
once a sticker design is agreed for the initial tea type (Green) we will require additional files for each tea type that we stock. Just the tea type (Green) to be updated - the rest of the design to stay the same. The tea types we stock are listed below
Green
Black
Oolong
White
Herbal
Blended
Happy to answer any questions and aim to give feedback daily! Thank you for your interest

```html
<!DOCTYPE html>
<html lang="en">
<head>
<meta charset="utf-8">
<title>BrookLeafs – Green Leaf Tea Sticker</title>
<link rel="stylesheet" href="https://fonts.googleapis.com/css2?family=Jost:wght@400;500&family=Josefin+Sans:wght@600&display=swap">
<style>
  :root {
    --bg: #dcdcdc;
    --leaf-black: #141414;
    --leaf-pattern: #232323;
    --green: #8cc63f;
    --green-light: #c8e68a;
    --orange: #f7941d;
    --white: #ffffff;
  }
  html, body {
    margin: 0;
    padding: 0;
    overflow: hidden;
  }
  body {
    width: 1200px;
    height: 1200px;
    background: var(--bg);
  }
  .sticker {
    display: block;
    width: 1200px;
    height: 1200px;
  }
  .sticker__body { fill: url(#leafFill); }
  .sticker__rim { fill: none; stroke: url(#rimGradient); stroke-width: 26; stroke-linejoin: round; }
  .sticker__stem { fill: var(--orange); }
  .sticker__url,
  .sticker__place {
    font-family: "Jost", sans-serif;
    font-weight: 400;
    font-size: 26px;
    letter-spacing: 0.5px;
    fill: var(--white);
  }
  .brand-name {
    font-family: "Jost", sans-serif;
    font-weight: 500;
    font-size: 74px;
    fill: var(--orange);
  }
  .tea-type__pill { fill: none; stroke: var(--green); stroke-width: 4; }
  .tea-type__label {
    font-family: "Josefin Sans", sans-serif;
    font-weight: 600;
    font-size: 26px;
    letter-spacing: 1.5px;
    fill: var(--green);
  }
  .tagline { font-family: "Jost", sans-serif; font-weight: 400; fill: var(--white); }
  .tagline__small { font-size: 32px; }
  .tagline__big { font-size: 50px; }
  .tagline__tiny { font-size: 24px; }
  .tagline__line { font-size: 46px; }
</style>
</head>
<body>
<svg class="sticker" viewBox="0 0 1200 1200" xmlns="http://www.w3.org/2000/svg">
  <defs>
    <linearGradient id="rimGradient" x1="0" y1="1" x2="1" y2="0">
      <stop offset="0" stop-color="var(--green)"/>
      <stop offset="0.55" stop-color="var(--green-light)"/>
      <stop offset="1" stop-color="var(--green)"/>
    </linearGradient>
    <radialGradient id="leafFill" cx="0.5" cy="0.55" r="0.6">
      <stop offset="0" stop-color="var(--leaf-pattern)"/>
      <stop offset="1" stop-color="var(--leaf-black)"/>
    </radialGradient>
  </defs>

  <g class="sticker__leaf">
    <path class="sticker__body" role="img" aria-label="Subtle dark tea leaf pattern fills the leaf"
          d="M 249 949 C 121 847 104 592 274 456 C 444 320 818 320 1056 150 C 1005 456 784 847 478 983 C 376 1017 291 991 249 949 Z"/>
    <path class="sticker__rim"
          d="M 249 949 C 121 847 104 592 274 456 C 444 320 818 320 1056 150 C 1005 456 784 847 478 983 C 376 1017 291 991 249 949 Z"/>
    <path class="sticker__stem"
          d="M 320 720 C 238 792 198 930 236 1070 C 226 945 252 820 320 720 Z"/>
  </g>

  <text class="sticker__url" transform="translate(210 680) rotate(-47)">www.brookleafs.co.uk</text>

  <g class="tagline" transform="translate(735 372) rotate(-4)">
    <text class="tagline__small" x="0" y="0">Leaf</text>
    <text class="tagline__big" x="60" y="0">Tea</text>
    <text class="tagline__tiny" x="136" y="-4">and</text>
    <text class="tagline__line" x="0" y="48">Infusions</text>
  </g>

  <g class="brand">
    <text class="brand-name" x="570" y="702" text-anchor="middle">BrookLeafs</text>
  </g>

  <g class="tea-type">
    <rect class="tea-type__pill" x="405" y="745" width="330" height="46" rx="23"/>
    <text class="tea-type__label" x="570" y="778" text-anchor="middle">GREEN LEAF TEA</text>
  </g>

  <text class="sticker__place" transform="translate(352 942) rotate(-18)">Welbury, England</text>
</svg>
</body>
</html>
```